Business card design needed

We are 2 artists starting up a studio by the water in Sydney ...where we can work and display our art...would like the back ground to be Navy and white stripe...nautical...and the name The Paint Hut to be bold and the main wording...not nautical...if possible thought the A for art could be an easel ...ie the capital A using the cross bar as the platform that paint would be circles of colour....would like the main wording in Black but the easel A in colour
Hope u are able to help
thanku Lorna Vesk
as I will be away in a week for 4 weeks could u please send all info to Mira Colbins email....she can contact me and we can go ahead asap....

Artists

THE PAINT HUT

Hallorans Oar House
The Reach..17 Kellaby Rd..Dunrook 2091 Sydney

Mir Colbin..0437819025..miracolbin@mailnest.example
Lorn Vesk...0429573816..lvesk@harborlink.example

```html
<!DOCTYPE html>
<html lang="en">
<head>
<meta charset="utf-8">
<title>The Paint Hut – Business Card</title>
<link rel="stylesheet" href="https://fonts.googleapis.com/css2?family=Cabin:wght@400;500&display=swap">
<style>
  :root {
    --page: #ffffff;
    --stripe-blue: #079fdc;
    --sky-circle: #6fcff6;
    --navy-text: #2a2a6c;
    --ink: #0a0a0a;
    --paper: #ffffff;
  }
  html, body {
    margin: 0;
    padding: 0;
    width: 1200px;
    height: 1000px;
    overflow: hidden;
    background: var(--page);
  }
  .card-canvas {
    display: block;
    width: 1200px;
    height: 1000px;
    font-family: "Cabin", sans-serif;
  }
  .stripe { fill: var(--stripe-blue); }
  .sea-band { fill: var(--stripe-blue); }
  .address-disc { fill: var(--sky-circle); }
  .wordmark {
    font-size: 63px;
    font-weight: 500;
    fill: var(--ink);
  }
  .address {
    font-size: 20px;
    font-weight: 400;
    fill: var(--navy-text);
  }
  .contact-name { font-size: 22px; font-weight: 400; fill: var(--paper); }
  .contact-line { font-size: 19px; font-weight: 400; fill: var(--paper); }
</style>
</head>
<body>
<svg class="card-canvas" viewBox="0 0 1200 1000" xmlns="http://www.w3.org/2000/svg">
  <defs>
    <clipPath id="card-area">
      <rect x="316" y="261" width="641" height="359"/>
    </clipPath>
    <pattern id="stripe-pattern" x="325" y="0" width="22.6" height="10" patternUnits="userSpaceOnUse">
      <rect class="stripe" x="0" y="0" width="11" height="10"/>
    </pattern>
  </defs>

  <g class="card" clip-path="url(#card-area)">
    <rect x="316" y="261" width="641" height="359" fill="var(--paper)"/>

    <!-- upper stripe band -->
    <rect x="325" y="261" width="420" height="56" fill="url(#stripe-pattern)"/>

    <!-- lower stripe band -->
    <rect x="325" y="440" width="632" height="80" fill="url(#stripe-pattern)"/>

    <!-- solid band holding the contacts -->
    <rect class="sea-band" x="316" y="514" width="641" height="106"/>

    <!-- address disc -->
    <circle class="address-disc" cx="855" cy="340" r="117"/>
  </g>

  <text class="wordmark" x="347" y="411">The Paint Hut</text>

  <g class="address" text-anchor="end">
    <text x="937" y="295">THE PAINT HUT</text>
    <text x="937" y="321">Hallorans Oar House</text>
    <text x="937" y="347">The Reach</text>
    <text x="937" y="373">17 Kellaby Rd</text>
    <text x="937" y="399">Dunrook 2091</text>
    <text x="937" y="425">Sydney</text>
  </g>

  <g class="contact contact-first">
    <text class="contact-name" x="351" y="546">Lorn Vesk</text>
    <text class="contact-line" x="351" y="571">0429573816</text>
    <text class="contact-line" x="351" y="597">lvesk@harborlink.example</text>
  </g>

  <g class="contact contact-second">
    <text class="contact-name" x="602" y="546">Mir Colbin</text>
    <text class="contact-line" x="602" y="571">0437819025</text>
    <text class="contact-line" x="602" y="597">miracolbin@mailnest.example</text>
  </g>
</svg>
</body>
</html>
```